Velborne Systems needs a business card

The logo we have uploaded is going to be the image centered on the back.
The business card color is going to be black. Increase the contrast in the logo and lettering so the grey stands out from the black and is more readable. Keep the shadow effect if you can.
On the front, the only part of the logo that should be used is the Egyptian character. We would like the following information included: Name (first last), Title, Phone number, email and company name (Velborne Systems).
The images of colored sound waves we uploaded is a concept we would like implemented on the front as well but please do not use the exact image. It is for guideline purposes.
Get creative with the empty space. We are a technology company that deals with sound and lights. Please not too busy.
Thank you, we look forward to all your submissions.

```html
<!DOCTYPE html>
<html lang="en">
<head>
<meta charset="utf-8">
<title>Velborne Systems – Business Card Front</title>
<link href="https://fonts.googleapis.com/css2?family=Exo+2:wght@400;500;600&display=swap" rel="stylesheet">
<style>
  :root {
    --page-bg: #e4e6ea;
    --card-dark: #272727;
    --brand-red: #ea3036;
    --swoosh-grey: #8e8e8e;
    --swoosh-light: #d8d8d8;
    --ink-white: #ffffff;
  }
  * { margin: 0; padding: 0; box-sizing: border-box; }
  html, body {
    width: 1200px; height: 840px; overflow: hidden;
    background: var(--page-bg);
    font-family: "Exo 2", sans-serif;
  }
  .card {
    position: absolute; left: 100px; top: 130px;
    width: 1000px; height: 580px;
    background: var(--card-dark);
    overflow: hidden;
    box-shadow: 0 10px 30px rgba(0,0,0,0.25);
  }
  .card-waves { position: absolute; inset: 0; width: 1000px; height: 580px; }
  .brand {
    position: absolute; right: 110px; top: 80px;
    display: flex; align-items: center; gap: 14px;
    color: var(--ink-white); font-weight: 600; font-size: 32px; letter-spacing: 1px;
  }
  .brand-mark { width: 24px; height: 24px; background: var(--brand-red); }
  .identity {
    position: absolute; right: 100px; top: 170px;
    text-align: right; color: var(--ink-white);
  }
  .identity-name { font-size: 30px; font-weight: 500; letter-spacing: 1.5px; text-transform: uppercase; line-height: 36px; }
  .identity-title { font-size: 21px; font-weight: 400; line-height: 26px; }
  .address {
    position: absolute; right: 40px; top: 330px;
    text-align: right; color: var(--ink-white); font-style: normal;
    font-size: 20px; line-height: 30px; letter-spacing: 0.5px;
  }
  .contacts {
    position: absolute; left: 95px; top: 408px;
    list-style: none; color: var(--ink-white);
    font-size: 20px; letter-spacing: 1px;
  }
  .contacts li { display: flex; align-items: center; gap: 14px; height: 31px; }
  .contacts svg { width: 19px; height: 19px; fill: var(--ink-white); flex: none; }
</style>
</head>
<body>
  <article class="card">
    <svg class="card-waves" viewBox="0 0 1000 580" aria-hidden="true">
      <defs>
        <linearGradient id="swoosh-sheen" x1="0" y1="1" x2="1" y2="0">
          <stop offset="0" stop-color="var(--swoosh-grey)"/>
          <stop offset="0.5" stop-color="var(--swoosh-light)"/>
          <stop offset="1" stop-color="var(--swoosh-grey)"/>
        </linearGradient>
      </defs>
      <path class="wave-red" fill="var(--brand-red)"
            d="M0,380 C120,320 260,290 400,300 C560,312 640,360 760,330 C880,320 960,270 1000,200 L1000,580 L0,580 Z"/>
      <path class="swoosh-right" fill="url(#swoosh-sheen)"
            d="M1000,160 C960,245 880,300 720,322 C880,312 965,258 1000,192 Z"/>
      <path class="swoosh-left" fill="url(#swoosh-sheen)"
            d="M0,470 C30,420 80,380 160,350 C70,390 30,450 20,580 L0,580 Z"/>
    </svg>

    <div class="brand"><span class="brand-mark"></span><span class="brand-name">Velborne Systems</span></div>

    <div class="identity">
      <p class="identity-name">Marcus Delaney</p>
      <p class="identity-title">Managing Director</p>
    </div>

    <address class="address">
      207.9th floor,Arlen<br>Corven Road NTH
    </address>

    <ul class="contacts">
      <li><svg viewBox="0 0 24 24"><path d="M6.6 10.8a15 15 0 0 0 6.6 6.6l2.2-2.2c.3-.3.7-.4 1-.2 1.1.4 2.3.6 3.6.6.6 0 1 .4 1 1V20c0 .6-.4 1-1 1C10.6 21 3 13.4 3 4c0-.6.4-1 1-1h3.5c.6 0 1 .4 1 1 0 1.3.2 2.5.6 3.6.1.3 0 .7-.2 1z"/></svg>014 562 7830</li>
      <li><svg viewBox="0 0 24 24"><path d="M7 1h10a2 2 0 0 1 2 2v18a2 2 0 0 1-2 2H7a2 2 0 0 1-2-2V3a2 2 0 0 1 2-2zm0 3v15h10V4zm5 16.2a1 1 0 1 0 0 .01z"/></svg>014 562 7830</li>
      <li><svg viewBox="0 0 24 24"><path d="M6 2h9l3 3v5h2a2 2 0 0 1 2 2v8a2 2 0 0 1-2 2H4a2 2 0 0 1-2-2v-8a2 2 0 0 1 2-2h2zm2 2v6h8V6h-2V4zm-1 10v2h2v-2zm4 0v2h2v-2zm4 0v2h2v-2z"/></svg>014 562 7830</li>
      <li><svg viewBox="0 0 24 24"><path d="M2 5h20v14H2zm2 2v.5l8 5.5 8-5.5V7zm0 3v7h16v-7l-8 5.5z"/></svg>hello@velbornesys.com</li>
      <li><svg viewBox="0 0 24 24"><path d="M12 2a10 10 0 1 0 0 20 10 10 0 0 0 0-20zm6.9 6h-2.9a15 15 0 0 0-1.4-3.6A8 8 0 0 1 18.9 8zM12 4c.8 1.2 1.5 2.5 1.9 4h-3.8c.4-1.5 1.1-2.8 1.9-4zM4.3 14a8 8 0 0 1 0-4h3.4a16 16 0 0 0 0 4zm.8 2h2.9c.3 1.3.8 2.5 1.4 3.6A8 8 0 0 1 5.1 16zM8 8H5.1a8 8 0 0 1 4.3-3.6C8.8 5.5 8.3 6.7 8 8zm4 12c-.8-1.2-1.5-2.5-1.9-4h3.8c-.4 1.5-1.1 2.8-1.9 4zm2.3-6H9.7a14 14 0 0 1 0-4h4.6a14 14 0 0 1 0 4zm.3 5.6c.6-1.1 1.1-2.3 1.4-3.6h2.9a8 8 0 0 1-4.3 3.6zM16.3 14a16 16 0 0 0 0-4h3.4a8 8 0 0 1 0 4z"/></svg>www.velbornesys.com</li>
    </ul>
  </article>
</body>
</html>
```